New Website for IT Services Business

We need an uncoded web design for a new company based in Australia called "Falcon Tech". We offer specialised point of sale (POS) support to the hospitality industry. We already support hundreds of cafes and restaurants. We are also about to launch and promote a range of new services with the offering of General IT Support being the most important. Other additional services to be offered are Falcon Cloud Backup, reselling and supporting Korvel Antivirus and Tresby Apps.

We have a logo design and our colour scheme is based on the logo with the addition of charcoal grey (see attached logos). We want the pages to reflect precision and efficiency with sharp characteristics. It must be professional but playful/fun elements are encouraged.

Our target audience is restaurant and cafe owners who are interested in finding high quality POS and IT support for their business.

The main call to action on the home page should be either 'Let's Meet For Coffee!' or 'Find out more (by completing a form)'. If you are unsure about what the general text should say then you can use 'Lorem Ipsum' where required.

The site must be viewable at different resolutions and on smart phones and tablets.

The website structure will be quite simple. We require:
- one impressive landing page. Visitors will quickly determine our services and that we provide a very high level of service while also offering value for money. Obviously a clear list of links (however/wherever you like) to the other pages.
- Simple pages with a similar layout for the following:
- Services - "POS & IT Support for the Hospitality Industry" being the main one. With complementary services also listed. Another call to action on this page with the option of 'Let's Meet For Coffee' or a "More information/Pricing" form to be completed by the visitor.
- Products - will be a small online storefront for a few simple products.
- About - Business background. 2x Directors with a photo and brief Bio.
- Downloads - A list of free files to download. Includes remote access client software.
- Contact Us - Mailing address, Email addresses and Support phone number.

Please feel free to ask any questions about the design. I will assist as much as possible.

Thank you for viewing. We promise to give constructive feedback to every person who submits a design. Thank you so much.

Target Market(s)

Restaurant and Cafe owners.

Industry/Entity Type

Hospitality

Requirements
Must have
• - Viewable on different resolutions and on smart phones and tablets.
- Clear call to action of EITHER 'Let's Meet For Coffee' or a "More information/Pricing" form to be completed by the visitor.

```html
<!DOCTYPE html>
<html lang="en">
<head>
<meta charset="utf-8">
<title>Falcon Tech – POS &amp; IT Support</title>
<link rel="stylesheet" href="https://fonts.googleapis.com/css2?family=Cabin:wght@500;600;700&family=Arimo:wght@400;700&display=swap">
<style>
:root{
  --red:#e31b2f;
  --red-dark:#c8142a;
  --charcoal:#3a3a3a;
  --charcoal-deep:#2b2b2b;
  --ink:#222;
  --text:#444;
  --muted:#777;
  --paper:#fff;
  --paper-soft:#f4f4f4;
  --line:#d9d9d9;
}
*{margin:0;padding:0;box-sizing:border-box}
html,body{width:1200px;height:932px;overflow:hidden}
body{position:relative;background:var(--paper);font-family:"Arimo",Arial,sans-serif;color:var(--text)}
.top-strip{position:absolute;left:0;top:0;width:1200px;height:9px;background:var(--red)}
.stage{position:absolute;left:0;top:9px;width:1200px;height:557px;
  background:radial-gradient(ellipse at 75% 40%,#5a5a5a 0%,#444 40%,#333 100%)}
.site-footer{position:absolute;left:0;top:847px;width:1200px;height:85px;background:var(--charcoal);z-index:1}

/* header */
.site-header{position:absolute;left:127px;top:9px;width:945px;height:88px;background:linear-gradient(#fff,#f2f2f2);
  border-radius:0 0 8px 8px;box-shadow:0 2px 6px rgba(0,0,0,.35)}
.brand{position:absolute;left:17px;top:22px;display:flex;align-items:center;gap:10px}
.brand-dot{width:40px;height:40px;border-radius:50%;background:var(--red)}
.brand-name{font-family:"Cabin",sans-serif;font-weight:700;font-size:34px;color:var(--ink);letter-spacing:-1px}
.main-nav{position:absolute;left:281px;top:0;height:88px;display:flex;align-items:center}
.main-nav a{font-family:"Cabin",sans-serif;font-weight:600;font-size:16px;color:var(--ink);text-decoration:none;
  padding:0 19px;position:relative}
.main-nav a+a::before{content:"";position:absolute;left:0;top:4px;height:10px;border-left:1px dotted #aaa}
.main-nav a.is-current{background:var(--red);color:#fff;height:88px;width:120px;display:flex;align-items:center;justify-content:center;padding:0;margin-right:16px}
.main-nav a.is-current+a::before{display:none}

/* hero */
.hero-copy{position:absolute;left:137px;top:154px;font-family:"Cabin",sans-serif;letter-spacing:-.5px}
.hero-kicker{font-size:19px;font-weight:500;color:#111}
.hero-title{font-size:35px;font-weight:700;color:#fff;line-height:33px;margin-top:0;text-transform:uppercase;letter-spacing:-1px}
.hero-sub{font-size:26px;font-weight:700;color:#111;margin-top:0;letter-spacing:-.6px}
.cta-coffee{position:absolute;left:138px;top:279px;width:247px;height:54px;border-radius:6px;
  background:linear-gradient(#3a3a3a,#0e0e0e);border:1px solid #000;box-shadow:0 1px 0 rgba(255,255,255,.2) inset;
  display:flex;align-items:center;padding-left:27px;font-family:"Cabin",sans-serif;font-weight:600;font-size:19px;color:#fff;text-decoration:none;letter-spacing:-.5px}
.hero-art{position:absolute;left:632px;top:133px;width:432px;height:214px;border-radius:14px;
  background:radial-gradient(circle at 30% 45%,#1c1c1c 0%,#2d2d2d 30%,transparent 45%),
             radial-gradient(circle at 78% 50%,#e9eef5 0%,#a7c3e4 28%,transparent 46%)}
.slider-dots{position:absolute;left:579px;top:341px;display:flex;gap:6px}
.slider-dots span{width:16px;height:16px;border-radius:50%;background:#999}
.slider-dots span.is-active{background:#fff}

/* feature band */
.feature-band{position:absolute;left:136px;top:370px;width:928px;height:105px;border-radius:8px 8px 0 0;
  background:linear-gradient(var(--red),var(--red-dark));display:flex;color:#fff}
.feature{padding:13px 0 0 23px;position:relative}
.feature:nth-child(1){width:302px}
.feature:nth-child(2){width:314px}
.feature:nth-child(3){width:312px}
.feature+.feature::before{content:"";position:absolute;left:0;top:8px;bottom:0;width:2px;background:linear-gradient(rgba(0,0,0,.25),rgba(0,0,0,0))}
.feature h2{font-family:"Cabin",sans-serif;font-weight:600;font-size:21px;letter-spacing:-.5px}
.feature p{font-size:12px;line-height:15px;margin-top:5px;width:260px}
.feature a{display:inline-block;margin-top:11px;font-size:11.5px;color:#fff}

/* content panel */
.content-panel{position:absolute;left:124px;top:475px;width:950px;height:397px;background:var(--paper);
  border-radius:10px;box-shadow:0 0 6px rgba(0,0,0,.25);overflow:hidden;z-index:2}
.welcome{position:absolute;left:26px;top:40px;width:592px}
.section-title{font-family:"Cabin",sans-serif;font-weight:700;font-size:30px;color:var(--red);letter-spacing:-1px}
.welcome p{font-size:11.5px;line-height:15px;margin-top:15px;color:#333;letter-spacing:.3px}
.welcome .section-title+p{margin-top:11px}
.testimonials{position:absolute;left:639px;top:0;width:311px;height:332px;
  background:linear-gradient(90deg,#e9e9e9 0,#f6f6f6 10px,#fafafa 100%);padding:40px 0 0 24px}
.quote{display:flex;gap:9px;width:262px;padding:6px 0 6px}
.quote+.quote{border-top:1px dotted #999;margin-top:6px;padding-top:11px}
.quote-photo{flex:none;width:72px;height:72px;border:1px solid #ccc;background:linear-gradient(#bbb,#777)}
.quote-text{font-size:11.5px;line-height:15px;color:#333;letter-spacing:.3px}
.quote-name{font-weight:700;font-size:11.5px;margin-top:13px;color:#222}
.quote-role{font-size:9.5px;color:#444}
.quote-arrows{position:absolute;left:267px;top:286px;display:flex;gap:3px}
.round-btn{width:22px;height:22px;border-radius:50%;background:#333;display:flex;align-items:center;justify-content:center}
.partners{position:absolute;left:0;top:332px;width:950px;height:65px;background:linear-gradient(#fff,#eee);border-top:1px solid var(--line)}
.partner-arrow{position:absolute;top:17px;width:31px;height:31px}
.partner-arrow.is-prev{left:24px}
.partner-arrow.is-next{left:896px}
.partner-badges{position:absolute;left:74px;top:22px;display:flex;gap:44px}
.partner-badges span{width:100px;height:20px;border-radius:4px;background:#cfcfcf}
.partner-badges span:nth-child(3),.partner-badges span:nth-child(4){width:90px}

/* footer */
.footer-nav{position:absolute;left:125px;top:887px;font-size:10.5px;color:#eee;z-index:3}
.footer-nav a{color:#eee;text-decoration:none}
.copyright{position:absolute;left:125px;top:905px;font-size:10.5px;color:#eee;z-index:3}
.footer-brand{position:absolute;left:920px;top:886px;display:flex;align-items:center;gap:9px;z-index:3}
.footer-brand .brand-dot{width:34px;height:34px;background:#8a8a8a}
.footer-brand .brand-name{color:#8a8a8a;font-size:30px}
</style>
</head>
<body>
<div class="top-strip"></div>
<div class="stage"></div>
<footer class="site-footer"></footer>

<header class="site-header">
  <div class="brand"><span class="brand-dot"></span><span class="brand-name">Falcon Tech</span></div>
  <nav class="main-nav">
    <a class="is-current" href="#">Home</a>
    <a href="#">About Us</a>
    <a href="#">Services</a>
    <a href="#">Products</a>
    <a href="#">Downloads</a>
    <a href="#">Contact Us</a>
  </nav>
</header>

<section class="hero-copy">
  <p class="hero-kicker">We offer specialised point of sale</p>
  <h1 class="hero-title">POS &amp; IT Support for the<br>Hospitality Industry</h1>
  <p class="hero-sub">We support hundreds of cafes &amp; restaurants</p>
</section>
<a class="cta-coffee" href="#">Let's Meet For Coffee</a>
<div class="hero-art" role="img" aria-label="Illustration of Falcon Cloud Backup cloud, Korvel Antivirus and a ring of Tresby Apps icons"></div>
<div class="slider-dots"><span class="is-active"></span><span></span><span></span></div>

<section class="feature-band">
  <div class="feature"><h2>About Our Company</h2><p>Lorem ipsum dolor sit amet, consectetur adip-isicing elit...</p><a href="#">readmore →</a></div>
  <div class="feature"><h2>Our Services</h2><p>Lorem ipsum dolor sit amet, consectetur adip-isicing elit...</p><a href="#">readmore →</a></div>
  <div class="feature"><h2>Our Products</h2><p>Lorem ipsum dolor sit amet, consectetur adip-isicing elit...</p><a href="#">readmore →</a></div>
</section>

<main class="content-panel">
  <section class="welcome">
    <h2 class="section-title">Welcome to Falcon Tech</h2>
    <p>Lorem ipsum dolor sit amet, consectetur adipisicing elit, sed do eiusmod tempor incididunt ut labore et dolore magna aliqua. Ut enim ad minim veniam, quis nostrud exercitation ullamco laboris nisi ut aliquip ex ea commodo consequat. Duis aute irure dolor in reprehenderit in voluptate velit esse cillum dolore eu fugiat nulla pariatur. Excepteur sint occaecat cupidatat non proident, sunt in culpa qui officia deserunt mollit anim id est laborum.</p>
    <p>Lorem ipsum dolor sit amet, consectetur adipisicing elit, sed do eiusmod tempor incididunt ut labore et dolore magna aliqua. Ut enim ad minim veniam, quis nostrud exercitation ullamco laboris nisi ut aliquip ex ea commodo consequat. Duis aute irure dolor in reprehenderit in voluptate velit esse cillum dolore eu fugiat nulla pariatur. Excepteur sint occaecat cupidatat non proident, sunt in culpa qui officia deserunt mollit anim id est laborum.</p>
    <p>Lorem ipsum dolor sit amet, consectetur adipisicing elit, sed do eiusmod tempor incididunt ut labore et dolore magna aliqua. Ut enim ad minim veniam, quis nostrud exercitation ullamco laboris nisi ut aliquip ex ea commodo consequat.</p>
  </section>

  <aside class="testimonials">
    <h2 class="section-title">Testimonials</h2>
    <div class="quote">
      <div class="quote-photo" role="img" aria-label="Portrait photo of client"></div>
      <div><p class="quote-text">“onsectetur adipisicing elit, sed do eiusmod tempor incididunt ut labore...”</p><p class="quote-name">Megan Hollis</p><p class="quote-role">CEO</p></div>
    </div>
    <div class="quote">
      <div class="quote-photo" role="img" aria-label="Portrait photo of client"></div>
      <div><p class="quote-text">“onsectetur adipisicing elit, sed do eiusmod tempor incididunt ut labore...”</p><p class="quote-name">Megan Hollis</p><p class="quote-role">CEO</p></div>
    </div>
    <div class="quote-arrows">
      <span class="round-btn"><svg width="8" height="10" viewBox="0 0 8 10"><path d="M6 1 2 5l4 4" stroke="#fff" stroke-width="2" fill="none"/></svg></span>
      <span class="round-btn"><svg width="8" height="10" viewBox="0 0 8 10"><path d="M2 1l4 4-4 4" stroke="#fff" stroke-width="2" fill="none"/></svg></span>
    </div>
  </aside>

  <section class="partners" aria-label="Partners">
    <svg class="partner-arrow is-prev" viewBox="0 0 31 31"><circle cx="15.5" cy="15.5" r="14" fill="#fff" stroke="#222" stroke-width="2.5"/><path d="M18 9l-7 6.5 7 6.5" stroke="#222" stroke-width="3" fill="none"/></svg>
    <div class="partner-badges"><span></span><span></span><span></span><span></span><span></span><span></span></div>
    <svg class="partner-arrow is-next" viewBox="0 0 31 31"><circle cx="15.5" cy="15.5" r="14" fill="#fff" stroke="#222" stroke-width="2.5"/><path d="M13 9l7 6.5-7 6.5" stroke="#222" stroke-width="3" fill="none"/></svg>
  </section>
</main>

<nav class="footer-nav"><a href="#">Home</a> . <a href="#">About Us</a> . <a href="#">Services</a> . <a href="#">Products</a> . <a href="#">Downloads</a> . <a href="#">Contact Us</a></nav>
<p class="copyright">Copyright © 2012-2013 Falcon Tech, All rights reserved!</p>
<div class="footer-brand"><span class="brand-dot"></span><span class="brand-name">Falcon Tech</span></div>
</body>
</html>
```